Brochure Design

I need a brochure that I can give to prospective clients during meetings and shows. My company website is www.brightpathmarketingpro.com

There is information to help with the creation of the brochure. Additionally, I will be attaching the new company logo. The website is being fixed behind the scenes to incorporate the new logo and color schemes. Please allow the colors in the brochure to the logo and not the current website.

Thanks!

```html
<!DOCTYPE html>
<html lang="en">
<head>
<meta charset="utf-8">
<title>Brightpath Brochure</title>
<link href="https://fonts.googleapis.com/css2?family=Exo+2:wght@300;400;500&family=Montserrat:wght@300;400;600&display=swap" rel="stylesheet">
<style>
:root{
  --page:#ffffff;
  --backdrop:#e9eaec;
  --lime:#a6cf1c;
  --green:#1e9a3c;
  --green-dark:#3f8f2a;
  --blue:#2a7cc2;
  --red:#c8202a;
  --text:#5b5d60;
  --text-dark:#333538;
}
*{margin:0;padding:0;box-sizing:border-box}
html,body{width:1200px;height:801px;overflow:hidden;background:var(--backdrop)}
.brochure{position:absolute;left:32px;top:34px;width:1420px;height:916px;transform:scale(.8);transform-origin:0 0;background:var(--page);box-shadow:0 2px 10px rgba(0,0,0,.25);font-family:"Exo 2",sans-serif}
.panel{position:absolute;top:0;height:916px;overflow:hidden}
.panel-inside{left:0;width:709px}
.panel-cover{left:710px;width:710px;border-left:1px solid #e2e2e2}
.shapes{position:absolute;left:0;top:0}
.hero-art{position:absolute;left:160px;top:43px;width:430px;height:395px;background:radial-gradient(ellipse at 55% 60%,#5aa7df 0%,#bcd9ee 40%,rgba(255,255,255,0) 72%)}
.headline{position:absolute;left:0;width:709px;top:438px;text-align:center;color:var(--red);font-size:20px;font-weight:400;line-height:25px;letter-spacing:.2px}
.service{position:absolute;width:236px}
.service .icon{position:absolute;left:-52px;top:-2px}
.service h3{font-size:19.5px;font-weight:400;color:var(--blue);line-height:24px;margin-bottom:4px;white-space:nowrap}
.service p{font-family:"Montserrat",sans-serif;font-weight:300;font-size:10.2px;line-height:12.6px;color:var(--text);text-align:justify}
.footer-brand{position:absolute;left:42px;top:800px;width:130px;text-align:center}
.brand-name{font-family:"Exo 2",sans-serif;font-weight:400;color:var(--green-dark);white-space:nowrap}
.footer-brand .brand-name{font-size:17px;letter-spacing:2.5px;margin-top:6px}
.footer-divider{position:absolute;left:175px;top:815px;width:1px;height:75px;background:#9a9a9a}
.contact{position:absolute;left:192px;top:820px;font-family:"Montserrat",sans-serif;font-size:12px;line-height:16px;color:var(--text-dark)}
.contact li{list-style:none;position:relative;padding-left:14px;white-space:nowrap}
.contact li svg{position:absolute;left:0;top:3px}
.contact .phone{font-weight:600;margin-top:3px}
.contact .web{margin-top:3px}
.social{position:absolute;left:487px;top:851px;display:flex;gap:8px}
.social span{width:53px;height:35px;border-radius:5px;background:linear-gradient(#6fb2e6,#2b78bd)}
.cover-brand{position:absolute;left:420px;top:66px;width:260px;text-align:center}
.cover-brand .brand-name{font-size:32px;letter-spacing:4px;margin-top:10px}
.seo-art{position:absolute;left:80px;top:288px;width:560px;height:360px;background:radial-gradient(ellipse at 45% 45%,#4f86b8 0%,#9fbad3 35%,rgba(220,221,223,0) 70%)}
.tagline{position:absolute;left:0;width:710px;top:740px;text-align:center;color:var(--green);font-size:30px;font-weight:400;letter-spacing:.3px;white-space:nowrap}
.cover-web{position:absolute;right:30px;top:873px;font-family:"Montserrat",sans-serif;font-size:13.5px;color:var(--text-dark);padding-left:18px;white-space:nowrap}
.cover-web svg{position:absolute;left:0;top:3px}
</style>
</head>
<body>
<main class="brochure">
  <section class="panel panel-inside">
    <svg class="shapes" width="709" height="916" aria-hidden="true">
      <defs>
        <linearGradient id="grayFade" x1="0" y1="0" x2="0" y2="1">
          <stop offset="0" stop-color="#e4e5e6"/><stop offset="1" stop-color="#d6d7d9"/>
        </linearGradient>
        <linearGradient id="limeFade" x1="0" x2="1">
          <stop offset="0" stop-color="#a6cf1c"/><stop offset="1" stop-color="#d9ee8a"/>
        </linearGradient>
      </defs>
      <polygon points="0,388 709,341 709,730 660,773 0,773" fill="url(#grayFade)"/>
      <polygon points="0,341 200,341 150,388 0,388" fill="url(#limeFade)"/>
      <rect x="0" y="903" width="709" height="13" fill="var(--lime)"/>
      <rect x="0" y="903" width="709" height="4" fill="#6aa832"/>
    </svg>
    <div class="hero-art" role="img" aria-label="Business silhouettes standing on blue city buildings beside a rising green arrow on a grid"></div>

    <h2 class="headline">YOU WANT TO CONNECT WITH MORE CLIENTS.<br>WE HAVE THE SEO TOOLS YOU NEED TO MAKE THAT HAPPEN.</h2>

    <article class="service" style="left:90px;top:514px">
      <svg class="icon" width="42" height="42" viewBox="0 0 42 42" aria-hidden="true"><path d="M21 4a17 17 0 0 1 17 17h-9a8 8 0 0 0-8-8z" fill="#d9342b"/><path d="M38 21a17 17 0 0 1-17 17v-9a8 8 0 0 0 8-8z" fill="#2a7cc2"/><path d="M21 38A17 17 0 0 1 4 21h9a8 8 0 0 0 8 8z" fill="#4caf3c"/><path d="M4 21A17 17 0 0 1 21 4v9a8 8 0 0 0-8 8z" fill="#f2a81d"/></svg>
      <h3>Search Engine Optimization</h3>
      <p>Brightpath is an SEO company able to provide your business with practical SEO services and Search Engine Optimization solutions to help your business grow.</p>
    </article>
    <article class="service" style="left:415px;top:514px">
      <svg class="icon" width="42" height="42" viewBox="0 0 42 42" aria-hidden="true"><rect x="15" y="3" width="11" height="11" fill="#2a7cc2"/><rect x="5" y="16" width="11" height="11" fill="#f2a81d"/><rect x="18" y="16" width="11" height="11" fill="#d9342b"/><rect x="11" y="29" width="11" height="11" fill="#4caf3c"/><rect x="27" y="28" width="11" height="11" fill="#2a7cc2"/></svg>
      <h3>Advanced SEO Tools</h3>
      <p>Brightpath is an SEO company that offers Cutting edge SEO tools, SEO marketing, SEO training and Search Engine Optimization solutions in order to attract more web traffic and convert more sales for your business.</p>
    </article>
    <article class="service" style="left:90px;top:636px">
      <svg class="icon" width="42" height="42" viewBox="0 0 42 42" aria-hidden="true"><circle cx="21" cy="21" r="17" fill="#2a7cc2"/><path d="M21 4a17 17 0 0 1 17 17H21z" fill="#d9342b"/><path d="M38 21a17 17 0 0 1-17 17V21z" fill="#4caf3c"/><path d="M4 21A17 17 0 0 1 21 4v17z" fill="#f2a81d"/><circle cx="21" cy="21" r="7" fill="#fff"/></svg>
      <h3>Our SEO Services</h3>
      <p>Brightpath is an SEO company that helps clients to achieve higher search engine rankings by using SEO tools and providing SEO tips in order to promote business growth.</p>
    </article>
    <article class="service" style="left:415px;top:636px">
      <svg class="icon" width="42" height="42" viewBox="0 0 42 42" aria-hidden="true"><rect x="18" y="3" width="7" height="16" fill="#d9342b"/><rect x="23" y="17" width="16" height="7" fill="#2a7cc2"/><rect x="18" y="23" width="7" height="16" fill="#f2a81d"/><rect x="3" y="18" width="16" height="7" fill="#4caf3c"/></svg>
      <h3>Beyond our SEO Services</h3>
      <p>Brightpath is an SEO company that strongly believes in listening to the customer's Search Engine Optimization goals in order to provide customized SEO Services, SEO Tools and SEO Tips to achieve those goals.</p>
    </article>

    <div class="footer-brand">
      <svg width="44" height="44" aria-hidden="true"><circle cx="22" cy="22" r="20" fill="var(--lime)"/></svg>
      <div class="brand-name">BRIGHTPATH</div>
    </div>
    <div class="footer-divider"></div>
    <ul class="contact">
      <li><svg width="9" height="11" viewBox="0 0 9 11"><path d="M4.5 0a4 4 0 0 1 4 4c0 3-4 7-4 7s-4-4-4-7a4 4 0 0 1 4-4z" fill="var(--blue)"/><circle cx="4.5" cy="4" r="1.5" fill="#fff"/></svg>4817 Kalena Lane<br>Honolulu, HI 96815</li>
      <li class="phone"><svg width="10" height="9" viewBox="0 0 10 9"><path d="M1 3c0-2 8-2 8 0v1H7V3H3v1H1z" fill="var(--blue)"/><rect x="2" y="5" width="6" height="4" rx="1" fill="var(--blue)"/></svg>[808] 555 - 0142</li>
      <li class="web"><svg width="10" height="10" viewBox="0 0 10 10"><circle cx="5" cy="5" r="4.3" fill="none" stroke="var(--blue)"/><path d="M1 5h8M5 1v8" stroke="var(--blue)"/></svg>www.brightpathmarketingpro.com</li>
    </ul>
    <div class="social" aria-hidden="true"><span></span><span></span><span></span></div>
  </section>

  <section class="panel panel-cover">
    <svg class="shapes" width="710" height="916" aria-hidden="true">
      <defs>
        <linearGradient id="bandGray" x1="0" x2="1">
          <stop offset="0" stop-color="#e3e4e5"/><stop offset=".5" stop-color="#d4d5d7"/><stop offset="1" stop-color="#dedfe0"/>
        </linearGradient>
        <linearGradient id="limeWedge" x1="0" x2="1">
          <stop offset="0" stop-color="#a6cf1c"/><stop offset="1" stop-color="#dff08f"/>
        </linearGradient>
      </defs>
      <polygon points="80,256 710,256 710,688 40,688 0,658 0,330" fill="url(#bandGray)"/>
      <polygon points="430,855 710,855 710,903 390,903" fill="url(#limeWedge)"/>
      <rect x="0" y="903" width="710" height="13" fill="var(--lime)"/>
      <rect x="0" y="903" width="710" height="4" fill="#6aa832"/>
    </svg>
    <div class="cover-brand">
      <svg width="80" height="80" aria-hidden="true"><circle cx="40" cy="40" r="36" fill="var(--lime)"/></svg>
      <div class="brand-name">BRIGHTPATH</div>
    </div>
    <div class="seo-art" role="img" aria-label="Large blue SEO lettering with a globe, computer mouse and curved arrows circled by the words results, website, engine and optimization"></div>
    <h1 class="tagline">DIGITAL MARKETING AND SEO SERVICES</h1>
    <div class="cover-web"><svg width="12" height="12" viewBox="0 0 10 10"><circle cx="5" cy="5" r="4.3" fill="none" stroke="var(--blue)"/><path d="M1 5h8M5 1v8" stroke="var(--blue)"/></svg>www.brightpathmarketingpro.com</div>
  </section>
</main>
</body>
</html>
```